Website for Foodstuff Import-Export Company *

We need a website for our company which imports and sell ( edible oil , ketchup , mayonnaise and pulses ). our current website is brevonix.pl , we need a website which has corporate appearance with good quality products.

Target Market(s)

European Wholesalers , Supermarket Chains,

Coding

Coded - Design and coding required

Number of Pages Required

1 page

```html
<!DOCTYPE html>
<html lang="en">
<head>
<meta charset="utf-8">
<title>Brevonix – Foodstuff Import &amp; Export</title>
<link href="https://fonts.googleapis.com/css2?family=Montserrat:wght@600;700;800;900&family=Open+Sans:wght@400;600;700&display=swap" rel="stylesheet">
<style>
:root{
  --green:#3aa935;
  --green-dark:#1f8f3a;
  --green-light:#6cc24a;
  --orange:#f39423;
  --orange-light:#f6a53c;
  --pink:#e8456e;
  --ink:#222222;
  --text:#4a4a4a;
  --muted:#6b6b6b;
  --footer:#1e1e1e;
  --white:#ffffff;
  --blue-line:#4a90c8;
}
*{margin:0;padding:0;box-sizing:border-box}
html,body{width:1200px;height:4688px;overflow:hidden}
body{font-family:"Open Sans",Arial,sans-serif;color:var(--text);background:var(--white);position:relative}
.abs{position:absolute}
h1,h2,h3{font-family:"Montserrat",Arial,sans-serif}
.btn{position:absolute;display:flex;align-items:center;justify-content:center;font-family:"Montserrat",Arial,sans-serif;font-weight:700;font-size:14px;color:var(--white);background:var(--orange);border-radius:22px;text-transform:uppercase;letter-spacing:.3px}
/* top bar */
.topbar{top:0;left:0;width:1200px;height:29px;background:var(--green);color:var(--white);font-size:13px;font-weight:600;text-align:center;line-height:29px}
/* hero */
.hero{top:29px;left:0;width:1200px;height:800px}
.hero-photo{top:0;left:0;width:1200px;height:800px;background:radial-gradient(ellipse at 28% 48%,#c99a2e 0%,#7a4a16 28%,#3a2210 55%,#1b110a 80%)}
.brand{display:flex;align-items:center;gap:10px;font-family:"Montserrat",Arial,sans-serif;font-weight:700;font-size:30px;color:var(--green-light);letter-spacing:1px}
.brand .dot{width:22px;height:22px;border-radius:50%;background:var(--green-light)}
.nav{top:114px;left:572px;display:flex;gap:36px;font-size:18px;color:var(--white)}
.nav .active{font-weight:700}
.call{top:58px;left:752px;display:flex;align-items:center;gap:12px;color:var(--white);font-size:19px}
.call b{font-weight:700}
.call .ring{width:36px;height:36px;border-radius:50%;border:2px solid var(--green-light);display:flex;align-items:center;justify-content:center}
.hero-title{top:190px;left:698px;font-weight:900;font-size:50px;line-height:51px;color:var(--green-light);letter-spacing:.5px}
.slide-arrow{width:40px;height:40px;border-radius:50%;border:2px solid rgba(255,255,255,.7);display:flex;align-items:center;justify-content:center}
/* welcome */
.welcome-img{top:920px;left:148px;width:380px;height:360px;border-radius:50%;background:radial-gradient(circle,#b5662e 0%,#7c4a2a 45%,#3b5a2a 75%,#ffffff 76%)}
.divider-v{top:926px;left:557px;width:1px;height:345px;background:#dddddd}
.welcome h2{font-size:34px;font-weight:800;color:var(--green);top:930px;left:599px;white-space:nowrap}
.welcome h2 span{color:var(--orange)}
.welcome p{top:990px;left:599px;width:440px;font-size:13.5px;line-height:24px;color:var(--text)}
/* products */
.products-bg{top:1310px;left:0;width:1200px;height:832px}
.section-title{width:1200px;left:0;text-align:center;font-weight:800;font-size:38px}
.title-rule{width:66px;height:3px;left:567px}
.product{width:240px;text-align:center;color:var(--white)}
.product .pic{width:208px;height:208px;margin:0 auto;border-radius:50%;border:5px solid var(--white);box-shadow:0 0 0 3px rgba(255,255,255,.35)}
.product h3{font-size:16px;font-weight:700;margin-top:22px;letter-spacing:.5px;font-family:"Open Sans",Arial,sans-serif}
.product p{font-size:13.5px;line-height:21px;margin:8px auto 0;width:200px;color:#e6f5dd}
.product .outline{margin:22px auto 0;width:124px;height:34px;border:2px solid var(--white);border-radius:18px;font-family:"Montserrat",Arial,sans-serif;font-size:11px;font-weight:700;display:flex;align-items:center;justify-content:center}
/* mission */
.mission h2{top:2216px;left:144px;font-size:38px;font-weight:800;color:var(--green)}
.mission ul{list-style:none;top:2282px;left:144px;width:420px}
.mission li{display:flex;gap:14px;font-size:13.5px;line-height:18px;margin-bottom:17px;color:var(--text)}
.mission li i{flex:0 0 18px;height:18px;border-radius:50%;background:var(--green);margin-top:1px;display:flex;align-items:center;justify-content:center}
.mission-ring{top:2224px;left:628px;width:426px;height:426px;border-radius:50%;border:2px dashed var(--green)}
.mission-photo{top:2238px;left:642px;width:398px;height:398px;border-radius:50%;background:radial-gradient(circle at 55% 45%,#d9d34a 0%,#6d7a8a 40%,#2f3f5a 80%)}
/* testimonial */
.client-bg{top:2756px;left:0;width:1200px;height:672px}
.quote-card{top:2981px;left:266px;width:668px;height:276px;background:var(--white);border-radius:6px;box-shadow:0 6px 20px rgba(0,0,0,.15)}
.quote-text{top:3020px;left:340px;width:520px;text-align:center;font-size:16.5px;line-height:27px;color:#555}
.quote-name{top:3146px;left:512px;font-size:14px;color:#555}
.qmark{font-family:Georgia,serif;font-weight:700;font-size:60px;color:var(--ink);line-height:1}
.avatar{top:3196px;left:542px;width:116px;height:116px;border-radius:50%;border:4px solid var(--white);background:radial-gradient(circle,#8a8f98 0%,#4a5260 100%)}
/* blog */
.blog-title{top:3510px;color:var(--ink)}
.card{width:288px;height:378px;background:var(--white);box-shadow:0 2px 10px rgba(0,0,0,.12)}
.card .pic{position:absolute;top:10px;left:10px;width:268px;height:170px}
.card .date{position:absolute;top:10px;left:24px;width:44px;height:48px;background:var(--green);color:var(--white);font-family:"Montserrat",Arial,sans-serif;font-weight:700;font-size:13px;line-height:16px;text-align:center;padding-top:8px}
.card h3{position:absolute;top:204px;left:18px;width:250px;font-size:14.5px;line-height:21px;font-weight:700;color:var(--ink)}
.card p{position:absolute;top:258px;left:18px;width:255px;font-size:13px;line-height:20px;color:var(--text)}
.card .read{position:absolute;top:330px;left:18px;width:120px;height:33px;border:2px solid #3b4c6b;font-family:"Montserrat",Arial,sans-serif;font-size:11px;font-weight:700;color:#3b4c6b;display:flex;align-items:center;justify-content:center}
/* footer */
.footer{top:4130px;left:0;width:1200px;height:558px;background:var(--footer);color:#dddddd}
.footer h3{font-size:18px;font-weight:700;color:var(--white);font-family:"Montserrat",Arial,sans-serif}
.contact-list{list-style:none;font-size:14px;line-height:19px}
.contact-list li{display:flex;gap:14px;margin-bottom:12px}
.contact-list svg{flex:0 0 18px}
.social{display:flex;gap:10px}
.social span{width:32px;height:32px;border-radius:50%;border:2px solid #dddddd}
.subscribe{top:4296px;left:757px;width:300px;height:44px;border:1px solid #888;display:flex}
.subscribe span{flex:1;font-size:11px;color:#ccc;padding:14px 18px}
.subscribe b{width:56px;border-left:1px solid #888;display:flex;align-items:center;justify-content:center}
.foot-links{top:4562px;left:0;width:1200px;text-align:center;font-size:14px;color:#dddddd}
.copyright{top:4602px;left:0;width:1200px;text-align:center;font-size:14px;color:#dddddd}
</style>
</head>
<body>

<div class="abs topbar">Brevonix sp. z o.o. NIP: 5550001234 KRS:0000123456</div>

<section class="abs hero">
  <div class="abs hero-photo" role="img" aria-label="Bottles of sunflower oil with sunflowers on a rustic wooden table"></div>
  <svg class="abs" style="top:600px;left:0" width="1200" height="200" viewBox="0 0 1200 200">
    <path d="M0 100 Q520 260 1200 60 L1200 200 L0 200 Z" fill="var(--green)"/>
    <path d="M0 100 Q520 240 1200 100 L1200 200 L0 200 Z" fill="var(--white)"/>
  </svg>
  <div class="abs brand" style="top:114px;left:145px"><span class="dot"></span>BREVONIX</div>
  <div class="abs call">
    <span class="ring"><svg width="16" height="16" viewBox="0 0 24 24"><path d="M6.6 10.8a15.1 15.1 0 006.6 6.6l2.2-2.2a1 1 0 011-.25 11.4 11.4 0 003.6.57 1 1 0 011 1V20a1 1 0 01-1 1A17 17 0 013 4a1 1 0 011-1h3.5a1 1 0 011 1 11.4 11.4 0 00.57 3.6 1 1 0 01-.25 1z" fill="var(--green-light)"/></svg></span>
    <span>Call <b>+48712345678</b></span>
    <svg style="margin-left:30px" width="22" height="22" viewBox="0 0 24 24"><circle cx="10" cy="10" r="7" fill="none" stroke="#fff" stroke-width="3"/><path d="M15 15l6 6" stroke="#fff" stroke-width="3" stroke-linecap="round"/></svg>
  </div>
  <nav class="abs nav"><span class="active">Home</span><span>About Us</span><span>Products</span><span>Blog</span><span>Contact Us</span></nav>
  <h1 class="abs hero-title">BEST NATURAL<br>NUTRITIONAL<br>SOURCES OF<br>VITAMIN E</h1>
  <div class="btn" style="top:413px;left:699px;width:160px;height:42px;border-radius:2px">Learn More</div>
  <div class="abs slide-arrow" style="top:420px;left:64px"><svg width="14" height="14" viewBox="0 0 14 14"><path d="M9 2L4 7l5 5" stroke="#fff" stroke-width="2" fill="none"/></svg></div>
  <div class="abs slide-arrow" style="top:413px;left:1096px"><svg width="14" height="14" viewBox="0 0 14 14"><path d="M5 2l5 5-5 5" stroke="#fff" stroke-width="2" fill="none"/></svg></div>
</section>

<section class="welcome">
  <div class="abs welcome-img" role="img" aria-label="Arrangement of spoons filled with beans, lentils and pulses"></div>
  <div class="abs divider-v"></div>
  <h2 class="abs">WELCOME TO <span>BREVONIX</span></h2>
  <p class="abs">BREVONIX is a manufacturing and trading company in Wrocław , Poland. We established longer and closer working relationships with our clients and supplier not only provide immediate and reliable service but to continually exceed expectations and goals. We create commercial flows, import and export products, arranging and managing international projects with our partners. Supported our network, we are able to integrate all these functions with our fruitful experience. Our numerous competencies allow</p>
  <div class="btn" style="top:1212px;left:598px;width:154px;height:40px">Learn More</div>
</section>

<section>
  <svg class="abs products-bg" width="1200" height="832" viewBox="0 0 1200 832">
    <defs><linearGradient id="pg" x1="0" y1="0" x2="0" y2="1"><stop offset="0" stop-color="#7cc44a"/><stop offset=".5" stop-color="#3ea63a"/><stop offset="1" stop-color="#2a9a3a"/></linearGradient></defs>
    <path d="M0 0 Q600 140 1200 0 L1200 832 Q600 700 0 832 Z" fill="url(#pg)"/>
    <path d="M0 832 Q600 700 1200 832 L1200 800 Q600 690 0 800 Z" fill="#2a9a2a"/>
  </svg>
  <h2 class="abs section-title" style="top:1450px;color:var(--white)">OUR PRODUCTS</h2>
  <div class="abs title-rule" style="top:1513px;background:var(--white)"></div>
  <div class="abs product" style="top:1585px;left:119px">
    <div class="pic" role="img" aria-label="Bottle of edible oil with sunflowers" style="background:radial-gradient(circle,#f2c52a,#c88a18 60%,#7a5a1a)"></div>
    <h3>EDIBLE OIL</h3><p>Sed ut perspiciatis unde omnis iste natus voluptatem accusantium doloremque laudantium, totam rem</p><div class="outline">LEARN MORE</div>
  </div>
  <div class="abs product" style="top:1585px;left:359px">
    <div class="pic" role="img" aria-label="Bottles of ketchup with fresh tomatoes" style="background:radial-gradient(circle,#c7342a,#e8e2dc 70%)"></div>
    <h3>KETCHUP</h3><p>Sed ut perspiciatis unde omnis iste natus voluptatem accusantium doloremque laudantium, totam rem</p><div class="outline">LEARN MORE</div>
  </div>
  <div class="abs product" style="top:1585px;left:599px">
    <div class="pic" role="img" aria-label="Bowl of mayonnaise with lemon and herbs" style="background:radial-gradient(circle,#f7f2e0,#8fb0c0 75%)"></div>
    <h3>MAYONNAISE</h3><p>Sed ut perspiciatis unde omnis iste natus voluptatem accusantium doloremque laudantium, totam rem</p><div class="outline">LEARN MORE</div>
  </div>
  <div class="abs product" style="top:1585px;left:840px">
    <div class="pic" role="img" aria-label="Wooden spoons with assorted pulses and spices" style="background:radial-gradient(circle,#c86a2a,#6a3a22 70%)"></div>
    <h3>PULSES</h3><p>Sed ut perspiciatis unde omnis iste natus voluptatem accusantium doloremque laudantium, totam rem</p><div class="outline">LEARN MORE</div>
  </div>
</section>

<section class="mission">
  <h2 class="abs">OUR MISSION</h2>
  <ul class="abs">
    <li><i></i><span>Striving to meet the increasing and diversified demands of the customers.</span></li>
    <li><i></i><span>Being market leaders in defend market segments.</span></li>
    <li><i></i><span>Providing quality products &amp; reliable services and sourcing from reputed manu facturers.</span></li>
    <li><i></i><span>Becoming professional marketing partners for our principals to meet the objec tives of sales, market information, and customer service.</span></li>
    <li><i></i><span>Being the preferred supplier of our customers, with our products exceeding their quality requirements.</span></li>
    <li><i></i><span>Giving timely information to the customers regarding trends of the market dynamics.</span></li>
  </ul>
  <div class="btn" style="top:2608px;left:144px;width:154px;height:42px">Learn More</div>
  <div class="abs mission-ring"></div>
  <div class="abs mission-photo" role="img" aria-label="Warehouse worker in hard hat and safety vest holding a clipboard"></div>
</section>

<section>
  <svg class="abs client-bg" width="1200" height="672" viewBox="0 0 1200 672">
    <defs><linearGradient id="cg" x1="0" y1="0" x2="0" y2="1"><stop offset="0" stop-color="#f6a03a"/><stop offset=".55" stop-color="#f07a3e"/><stop offset="1" stop-color="#e6476e"/></linearGradient></defs>
    <path d="M0 130 Q600 -60 1200 130 L1200 560 Q600 760 0 560 Z" fill="url(#cg)"/>
    <path d="M0 560 Q600 760 1200 560 L1200 590 Q600 760 0 590 Z" fill="var(--orange-light)"/>
  </svg>
  <div class="abs" style="top:2770px;left:600px;width:500px;height:600px;opacity:.18;background:radial-gradient(circle,#ffffff,transparent 70%)" role="img" aria-label="Chef pouring sauce onto a plate"></div>
  <h2 class="abs section-title" style="top:2858px;color:var(--white)">OUR CLIENT SAY</h2>
  <div class="abs title-rule" style="top:2922px;background:var(--white)"></div>
  <svg class="abs" style="top:3090px;left:184px" width="22" height="34" viewBox="0 0 22 34"><path d="M18 3L5 17l13 14" stroke="#fff" stroke-width="3" fill="none"/></svg>
  <svg class="abs" style="top:3090px;left:994px" width="22" height="34" viewBox="0 0 22 34"><path d="M4 3l13 14L4 31" stroke="#fff" stroke-width="3" fill="none"/></svg>
  <div class="abs quote-card"></div>
  <div class="abs qmark" style="top:3006px;left:360px">“</div>
  <p class="abs quote-text">Nemo enim ipsam voluptatem quia voluptas sit aspernatur aut odit aut fugit, sed quia consequuntur magni dolores eos qui ratione voluptatem sequi nesciunt. Neque porro quisquam est, qui dolorem ipsum quia dolor sit amet, consectetur</p>
  <div class="abs quote-name">Adam Kowal –  BREVONIX</div>
  <div class="abs qmark" style="top:3140px;left:724px">”</div>
  <div class="abs avatar" role="img" aria-label="Portrait of the client"></div>
</section>

<section>
  <h2 class="abs section-title blog-title">LATEST BLOG</h2>
  <div class="abs title-rule" style="top:3575px;background:var(--blue-line)"></div>
  <article class="abs card" style="top:3627px;left:145px">
    <div class="pic" role="img" aria-label="Chicken nuggets with ketchup dip" style="background:linear-gradient(135deg,#e8a63a,#c0392b 60%,#2b4a7a)"></div>
    <div class="date">Oct<br>2020</div>
    <h3>SED UT PERSPICIATIS UNDE OMNIS ISTE NATUS</h3>
    <p>Sed ut perspiciatis unde omnis iste natus error sit voluptatem accusantium doloque laium, totam rem aperiam</p>
    <div class="read">READ MORE</div>
  </article>
  <article class="abs card" style="top:3643px;left:456px">
    <div class="pic" role="img" aria-label="Olive oil poured over a fresh salad" style="background:linear-gradient(135deg,#eeeeee,#d9a53a 50%,#5a9a3a)"></div>
    <div class="date">Oct<br>2020</div>
    <h3>SED UT PERSPICIATIS UNDE OMNIS ISTE NATUS</h3>
    <p>Sed ut perspiciatis unde omnis iste natus error sit voluptatem accusantium doloque laium, totam rem aperiam</p>
    <div class="read">READ MORE</div>
  </article>
  <article class="abs card" style="top:3627px;left:766px">
    <div class="pic" role="img" aria-label="Bowl of mayonnaise on a wooden board" style="background:radial-gradient(circle,#f6eecf,#7a5a3a 70%)"></div>
    <div class="date">Oct<br>2020</div>
    <h3>SED UT PERSPICIATIS UNDE OMNIS ISTE NATUS</h3>
    <p>Sed ut perspiciatis unde omnis iste natus error sit voluptatem accusantium doloque laium, totam rem aperiam</p>
    <div class="read">READ MORE</div>
  </article>
</section>

<footer class="abs footer"></footer>
<div class="abs brand" style="top:4296px;left:145px"><span class="dot"></span>BREVONIX</div>
<div class="abs social" style="top:4367px;left:174px" aria-label="Social links"><span></span><span></span><span></span></div>
<h3 class="abs" style="top:4196px;left:446px;font-size:18px;font-weight:700;color:#fff;font-family:'Montserrat',Arial,sans-serif">CONTACT US</h3>
<ul class="abs contact-list" style="top:4244px;left:446px;width:280px;list-style:none;font-size:14px;line-height:19px;color:#ddd">
  <li style="display:flex;gap:14px;margin-bottom:12px"><svg width="18" height="20" viewBox="0 0 24 24"><path d="M12 2a7 7 0 00-7 7c0 5 7 13 7 13s7-8 7-13a7 7 0 00-7-7zm0 9.5A2.5 2.5 0 1112 6.5a2.5 2.5 0 010 5z" fill="#fff"/></svg><span>ADDRESS<br>Ul. Lipowa 12 /4b</span></li>
  <li style="display:flex;gap:14px;margin-bottom:12px"><svg width="18" height="18" viewBox="0 0 24 24"><path d="M6.6 10.8a15.1 15.1 0 006.6 6.6l2.2-2.2a1 1 0 011-.25 11.4 11.4 0 003.6.57 1 1 0 011 1V20a1 1 0 01-1 1A17 17 0 013 4a1 1 0 011-1h3.5a1 1 0 011 1 11.4 11.4 0 00.57 3.6 1 1 0 01-.25 1z" fill="#fff"/></svg><span>Phone: +48712345678</span></li>
  <li style="display:flex;gap:14px;margin-bottom:12px"><svg width="18" height="18" viewBox="0 0 24 24"><path d="M3 5h18v14H3z" fill="#fff"/><path d="M3 5l9 7 9-7" stroke="#1e1e1e" stroke-width="2" fill="none"/></svg><span>E-mail: info@brevonix.pl</span></li>
  <li style="display:flex;gap:14px"><svg width="18" height="18" viewBox="0 0 24 24"><circle cx="12" cy="12" r="10" fill="#fff"/><path d="M12 6v6l4 2" stroke="#1e1e1e" stroke-width="2" fill="none"/></svg><span>Opening hours:<br><br>Man-Thurs: 9.30-17.30<br>Fri: 9.30-18.00</span></li>
</ul>
<h3 class="abs" style="top:4194px;left:757px;font-size:18px;font-weight:700;color:#fff;font-family:'Montserrat',Arial,sans-serif">JOIN OUR NEWSLETTER</h3>
<p class="abs" style="top:4242px;left:757px;width:300px;font-size:13px;line-height:19px;color:#ddd">Nemo enim ipsam voluptatem quia voluptas sit aspernatur aut odit aut fugit</p>
<div class="abs subscribe"><span>Enter your E - mail</span><b><svg width="20" height="16" viewBox="0 0 20 16"><path d="M1 8h16M11 2l6 6-6 6" stroke="#fff" stroke-width="2" fill="none"/></svg></b></div>
<div class="abs foot-links">Home &nbsp;|&nbsp; About Us &nbsp;|&nbsp; Products &nbsp;|&nbsp; Contact Us</div>
<div class="abs copyright">© 2020 Brevonix. All Rights Reserved</div>

</body>
</html>
```